Business card design for modern LaneScope agency

Hello,

I need a business card design for my company Harbor9Studio.
We mainly offer Vornix LaneScope Tours (360° Photography) and it should be a business card with following details:

Name: Tobias Merland
Number: +49 160 55 82 907
Mail: tobias@harbor9studio.example
website: harbor9studio.example

Main colour that we use is the red of the logo.
It´s also important to integrate the "Vornix Gold logo" as the person on this business card is a Vornix Gold photographer.

And if possible we would also like to integrate something like send us a sms or pingwell and we call you back. As the number is german but we sell now in Vienna, Austria.

We offer a good price but very high photography quality, as we are mostly students - that´s our concept.

Maybe an idea is to integrate something 360° on the back-side of the card, for example the photo attached (just an idea) or some great design.
See flyer (attached) and harbor9studio.example for inspiration, maybe use of the photo of me (attached) in a circle or something

I´m very excited for your designs and thanks a lot in advance!! :)

Target Market(s)

Shops, hotels, shopping centers, etc. in Vienna, Austria

Industry/Entity Type

Business

Contact Information for Business Card

double-sided, use red of the logo, 360° vornix lanescope certified photographer

Font styles to use
Serif
Sans Serif

Colors
ec1f27

Requirements
Nice to have
• maybe some 360° design on back-side
• maybe include photo of me in a circle or something or sketched in red colour

```html
<!DOCTYPE html>
<html lang="en">
<head>
<meta charset="utf-8">
<title>Harbor9Studio – Business Card</title>
<link href="https://fonts.googleapis.com/css2?family=Oswald:wght@500;600&family=Lato:wght@400;700&display=swap" rel="stylesheet">
<style>
  :root {
    --page: #e9e7e4;
    --card-dark: #2e2e2f;
    --card-mid: #3a3a3b;
    --brand-red: #ec1f27;
    --badge-gold: #c9a24a;
    --text-white: #f4f4f4;
    --text-grey: #a9a9ab;
    --line-grey: #bfbfc1;
  }
  * { margin: 0; padding: 0; box-sizing: border-box; }
  html, body { width: 1200px; height: 900px; overflow: hidden; background: var(--page); }
  body { position: relative; font-family: "Lato", Arial, sans-serif; }

  .card {
    position: absolute;
    width: 520px;
    height: 336px;
    border-radius: 4px;
    overflow: hidden;
    box-shadow: 0 10px 28px rgba(0,0,0,.22);
  }
  .card--front { left: 50px; top: 282px; background: var(--card-mid); }
  .card--back  { left: 630px; top: 282px; background: var(--card-dark); }

  /* Shared brand lockup: square + stacked name */
  .brand { position: absolute; display: flex; align-items: center; gap: 8px; }
  .brand__mark { width: 52px; height: 52px; background: var(--brand-red); flex: none; }
  .brand__name {
    font-family: "Oswald", "Arial Narrow", sans-serif; font-weight: 500;
    font-size: 25px; line-height: .95; letter-spacing: .5px;
    color: var(--text-grey); text-transform: uppercase;
  }

  /* Front: top band */
  .front-header {
    position: absolute; left: 0; top: 0; width: 100%; height: 158px;
    background: var(--card-dark);
  }
  .holder { position: absolute; left: 30px; top: 24px; }
  .holder__name {
    font-family: "Oswald", "Arial Narrow", sans-serif; font-weight: 600;
    font-size: 22px; letter-spacing: 1px; color: var(--text-white); line-height: 1;
  }
  .holder__role {
    display: inline-block; margin-top: 4px; padding: 1px 12px 2px 44px;
    background: var(--brand-red); color: var(--text-white);
    font-size: 11px; letter-spacing: 2px;
  }
  .front-header .brand { left: 78px; top: 82px; }
  .address {
    position: absolute; right: 26px; bottom: 16px; display: flex; align-items: center; gap: 8px;
    font-size: 13px; color: var(--text-white);
  }

  /* Front: lower band */
  .frame-corners { position: absolute; }
  .card--front .frame-corners { left: 30px; top: 180px; }
  .portrait {
    position: absolute; left: 66px; top: 200px; width: 92px; height: 92px; border-radius: 50%;
    border: 4px solid var(--brand-red);
    background: radial-gradient(circle at 50% 40%, #8c8580, #4d4a48);
  }
  .contacts { position: absolute; left: 224px; bottom: 14px; list-style: none; }
  .contacts li {
    display: flex; align-items: center; gap: 10px; margin-bottom: 12px;
    font-size: 14px; color: var(--text-white);
  }
  .contact-icon { width: 16px; height: 16px; flex: none; }
  .cert-badge {
    position: absolute; right: 26px; top: 184px; width: 40px; height: 40px; border-radius: 50%;
    background: var(--badge-gold);
  }

  /* Back */
  .card--back .frame-corners { left: 90px; top: 60px; }
  .card--back .brand { left: 190px; top: 116px; }
  .card--back .brand__mark { width: 62px; height: 62px; }
  .card--back .brand__name { font-size: 30px; }
  .back-holder { position: absolute; left: 128px; top: 190px; }
  .back-holder__name {
    font-family: "Oswald", "Arial Narrow", sans-serif; font-weight: 600;
    font-size: 19px; letter-spacing: 1px; color: var(--text-white); line-height: 1;
  }
  .back-holder__role { font-size: 11px; letter-spacing: 3px; color: var(--text-grey); margin-top: 4px; }
</style>
</head>
<body>

<section class="card card--front" aria-label="Business card front">
  <header class="front-header">
    <div class="holder">
      <div class="holder__name">TOBIAS MERLAND</div>
      <div class="holder__role">photographer</div>
    </div>
    <div class="brand">
      <span class="brand__mark"></span>
      <span class="brand__name">Harbor9<br>Studio</span>
    </div>
    <div class="address">
      <svg class="contact-icon" viewBox="0 0 16 16"><circle cx="8" cy="8" r="7.5" fill="var(--text-white)"/><path d="M8 3.5a3 3 0 0 0-3 3c0 2.3 3 5.8 3 5.8s3-3.5 3-5.8a3 3 0 0 0-3-3z" fill="var(--card-dark)"/><circle cx="8" cy="6.5" r="1.1" fill="var(--text-white)"/></svg>
      14 Kessler Lane, Vienna
    </div>
  </header>

  <svg class="frame-corners" width="160" height="132" viewBox="0 0 160 132" fill="none" stroke="var(--line-grey)" stroke-width="1.4">
    <path d="M0 14V0h14M146 0h14v14M160 118v14h-14M14 132H0v-14"/>
  </svg>
  <div class="portrait" role="img" aria-label="Round portrait photo of Tobias Merland"></div>

  <div class="cert-badge" role="img" aria-label="Vornix Gold badge – 360° Vornix LaneScope certified photographer"></div>

  <ul class="contacts">
    <li>
      <svg class="contact-icon" viewBox="0 0 16 16" fill="none" stroke="var(--text-white)" stroke-width="1.2"><circle cx="8" cy="8" r="7.3"/><path d="M5.5 4.5l1.5 1.5-.8 1a5 5 0 0 0 2.8 2.8l1-.8 1.5 1.5-1 1c-3 0-6-3-6-6z" fill="var(--text-white)" stroke="none"/></svg>
      +49 160 55 82 907
    </li>
    <li>
      <svg class="contact-icon" viewBox="0 0 16 16" fill="none" stroke="var(--text-white)" stroke-width="1.2"><circle cx="8" cy="8" r="7.3"/><rect x="4.5" y="5" width="7" height="5" rx=".5"/><path d="M7 11.5h2"/></svg>
      harbor9studio.example
    </li>
    <li>
      <svg class="contact-icon" viewBox="0 0 16 16" fill="none" stroke="var(--text-white)" stroke-width="1.2"><circle cx="8" cy="8" r="7.3"/><rect x="4.5" y="5.2" width="7" height="5.2"/><path d="M4.5 5.2L8 8l3.5-2.8"/></svg>
      tobias@harbor9studio.example
    </li>
  </ul>
</section>

<section class="card card--back" aria-label="Business card back">
  <svg class="frame-corners" width="340" height="216" viewBox="0 0 340 216" fill="none" stroke="var(--line-grey)" stroke-width="1.4">
    <path d="M0 14V0h14M326 0h14v14M340 202v14h-14M14 216H0v-14"/>
  </svg>
  <div class="brand">
    <span class="brand__mark"></span>
    <span class="brand__name">Harbor9<br>Studio</span>
  </div>
  <div class="back-holder">
    <div class="back-holder__name">TOBIAS MERLAND</div>
    <div class="back-holder__role">photographer</div>
  </div>
</section>

</body>
</html>
```